4D Little Lumen Luxury Ultrasound Billboard

Design a HIGH-END, MODERN billboard for my private prenatal ultrasound studio, 4D Little Lumen, located in Pace, Florida.
This billboard will be viewed by drivers traveling at highway speeds, so it must be extremely clean, simple, and readable within 6 seconds.
About My Business
4D Little Lumen is a private prenatal ultrasound studio specializing in:
Highest technology 4D/HD Ultrasounds
Early Gender Determination
Pregnancy Confirmation
I have been serving families for nearly 10 years and is known for creating a memorable experience, not just an ultrasound appointment.
Design Style
I DO NOT want:
Flowers
Leaves
Swirls
Glitter
Hearts everywhere
Busy backgrounds
Generic maternity stock graphics
I DO want:
Modern
Luxury
Upscale
Clean
Professional
Eye-catching
Premium medical spa feel
Colors
Use colors from my logo:
LOGO Green ( or a deep green)
Black
White
Soft Gold accents
Images:
Incorporate my professional headshot in a clean, modern way, logo, and the ultrasound images
Text
Keep wording minimal.
Primary Headline ( OPEN TO IDEAS) :
EXAMPLES ( WOULD RATHER SOMETHING MORE CATCHY)
" ADVANCED IMAGING. UNFORGETTABLE MOMENTS"
"MEET YOUR BABY BEFORE BIRTH"
Under headline:
4D Ultrasound • Early Gender • Pregnancy Confirmation
Business Name:
4D Little Lumen
Private Prenatal Ultrasound Studio
Phone Number:
850-471-5923
Important
This billboard must be readable in 5–6 seconds from a moving vehicle.
Less text is better.
The phone number and business name must be visible from a distance.
The design should feel like a premium brand that immediately tells expecting parents:
“This is where I go to see my baby.”
Files Provided
Official logo
Headshot
Ultrasound images
Don’t make this look like a medical office billboard.
Make it look like a luxury baby experience billboard. That’s what separates 4D Little Lumen from hospitals, OB offices, and all the new studios popping up around you. The emotional connection is what gets moms to book. ❤️
Billboard Size - 10.6” x 36”

```html
<!DOCTYPE html>
<html lang="en">
<head>
<meta charset="utf-8">
<title>4D Little Lumen – Billboard</title>
<link rel="stylesheet" href="https://fonts.googleapis.com/css2?family=Roboto+Condensed:wght@400;700&display=swap">
<style>
  :root {
    --backdrop: #dcdcdc;
    --white: #ffffff;
    --ink: #161616;
    --black: #000000;
    --gold: #cc9e3a;
    --brand-green: #55675e;
    --muted: #6a6a6a;
    --scan-light: #a8685a;
    --scan-dark: #3a1a14;
    --portrait-light: #d8d4cf;
    --portrait-dark: #8b857e;
  }
  * { margin: 0; padding: 0; box-sizing: border-box; }
  html, body {
    width: 1200px;
    height: 1200px;
    overflow: hidden;
    background: var(--backdrop);
  }
  .billboard {
    position: absolute;
    left: 75px;
    top: 446px;
    width: 1050px;
    height: 310px;
    background: var(--white);
    overflow: hidden;
    box-shadow: 0 2px 6px rgba(0,0,0,0.25);
  }
  .billboard-art {
    position: absolute;
    inset: 0;
    width: 1050px;
    height: 310px;
  }
  .brand {
    position: absolute;
    left: 45px;
    top: 96px;
    width: 265px;
    text-align: center;
  }
  .brand-name {
    font-family: "Roboto Condensed", sans-serif;
    font-weight: 700;
    font-size: 38px;
    line-height: 1;
    color: var(--brand-green);
  }
  .brand-tagline {
    margin-top: 10px;
    font-family: "Roboto Condensed", sans-serif;
    font-weight: 400;
    font-size: 12px;
    letter-spacing: 1.4px;
    color: var(--muted);
  }
  .phone {
    position: absolute;
    left: 47px;
    top: 199px;
    font-family: "Roboto Condensed", sans-serif;
    font-weight: 700;
    font-size: 50px;
    line-height: 1;
    color: var(--black);
  }
  .message {
    position: absolute;
    right: 38px;
    top: 155px;
    text-align: right;
    font-family: "Roboto Condensed", sans-serif;
    color: var(--ink);
  }
  .headline {
    font-weight: 700;
    font-size: 32px;
    line-height: 39px;
  }
  .services {
    margin-top: 6px;
    font-weight: 400;
    font-size: 16px;
  }
</style>
</head>
<body>
  <div class="billboard">
    <svg class="billboard-art" viewBox="0 0 1050 310" xmlns="http://www.w3.org/2000/svg">
      <defs>
        <radialGradient id="scan-tone" cx="50%" cy="35%" r="65%">
          <stop offset="0%" stop-color="var(--scan-light)"/>
          <stop offset="100%" stop-color="var(--scan-dark)"/>
        </radialGradient>
        <linearGradient id="portrait-tone" x1="0" y1="0" x2="0" y2="1">
          <stop offset="0%" stop-color="var(--portrait-light)"/>
          <stop offset="100%" stop-color="var(--portrait-dark)"/>
        </linearGradient>
      </defs>
      <path class="ultrasound-image" role="img" aria-label="3D ultrasound image of twin babies face to face"
            fill="url(#scan-tone)"
            d="M306 0 L745 0 C730 90 650 180 515 236 C420 205 335 110 306 0 Z"/>
      <path class="accent-stripe" fill="var(--black)"
            d="M510 238 C680 300 900 310 1050 304 L1050 288 C880 300 640 272 500 232 Z"/>
      <path class="gold-sweep" fill="var(--gold)"
            d="M737 0 L1050 0 L1050 292 C880 300 640 272 500 232 C640 175 722 90 737 0 Z"/>
      <rect class="headshot" role="img" aria-label="Professional headshot of the studio owner"
            x="895" y="0" width="118" height="146" fill="url(#portrait-tone)"/>
    </svg>

    <div class="brand">
      <div class="brand-name">4D Little Lumen</div>
      <div class="brand-tagline">PRENATAL ULTRASOUND STUDIO</div>
    </div>

    <div class="phone">850-471-5923</div>

    <div class="message">
      <div class="headline">ADVANCED IMAGING.<br>UNFORGETTABLE MOMENTS</div>
      <div class="services">4D Ultrasound • Early Gender • Pregnancy Confirmation</div>
    </div>
  </div>
</body>
</html>
```